Concept design for a tea business Labels

Hello, we are looking for concepts for our label/packaging for a tea business that has been in business now for over a year. We are a beachy, organic, "It's your moment. Enjoy it." type tea business. We have an online website (www.corvalbrewhouse.com.au) and sell at local markets around the Tarrowby Cove area.
We are looking to upgrade our label to look more professional, in a fun/beachy/chilled out style. (unlike the traditional tea labels).
We do loose leaf tea and iced tea consentrated syrups. We have a few different packages (please see website under "sizes and packaging" bottom left). We would like to experiement with various different size and shape of labels for different products, so would like a concept design for a label using our logo (see website front page bottom). There are no colour constraints.
We use the Quillan brand labels of the following sizes:
1. Pure Glass Rectangular Product Labels, Q4825, 100/Pack, 96 x 50.8 mm
2. Pure Glass Round Multi-purpose Labels, Q3907D, 240/Pack, 40 mm diameter
3.Pure Glass Square Product Labels, Q4861, 350/Pack, 35 x 35 mm
4. For bottles we use Grained Ivory Curved Labels, Q4839, 90/Pack, 57.2 x 77 mm
If you have any more questions, please don't hesitate to contact me
Updates
Hi All,
I am considering using a box like below for packing and doing a bit of a white/beachy feel to the packaging. Either using the rectangle or round circle labels. (circle labels from quillan 60mm diameter).

Reason: Hi All - Thank you so much for all your designs. While I have seen some really beautiful designs I am excited about, it seems there was a rush at the end with a number of new designs just submitted. I still haven't seen just one design I love for the label, so I would like the opportunity to work with some of the new designers to see if we can modify to suit the concept.
Would anyone like to try a concept label with a silhouette of one of the following wave/beach/teacup? I'm just exploring a different approach as I know it is difficult tying in the beach with tea - please think - chilled out beach hut with tea/iced tea, sunrise over ocean. I like the soft colour palette - beachy feel to it - ie. Pastels - blues, greens, whites, sandy, pinks, purples, greys - sunrises over ocean, maybe a white rustic wood feel - or any other icon from Tarrowby Cove - like the Norfolk Pine's along the beach - maybe in Silhouette.
Just some more ideas.
Thank you again for all your contributions!
Petra

```html
<!DOCTYPE html>
<html lang="en">
<head>
<meta charset="utf-8">
<title>Tarrowby Tea Company – Tin Labels</title>
<link rel="stylesheet" href="https://fonts.googleapis.com/css2?family=Noto+Sans:wght@400;700&display=swap">
<style>
  :root {
    --backdrop: #4b4b50;
    --peach: #e0b595;
    --peach-art: #e9c6ab;
    --sage: #b4c28e;
    --sage-art: #c3cfa2;
    --ink: #33261d;
    --label-white: #ffffff;
    --lid-grey: #d9d9db;
  }
  * { box-sizing: border-box; margin: 0; padding: 0; }
  html, body {
    width: 1200px;
    height: 1184px;
    overflow: hidden;
  }
  body {
    position: relative;
    background: var(--backdrop);
    font-family: "Noto Sans", Tahoma, sans-serif;
    color: var(--ink);
  }

  /* Rectangular tin labels */
  .label {
    position: absolute;
    border-radius: 12px;
    background: var(--peach);
  }
  .label--sage { background: var(--sage); }
  .label__brand {
    position: absolute;
    font-size: 12px;
  }
  .label__title {
    position: absolute;
    font-size: 23px;
    line-height: 1.05;
    letter-spacing: 0.2px;
  }
  .label__tagline {
    position: absolute;
    font-size: 12px;
  }
  .label__art {
    position: absolute;
    border-radius: 50% 50% 44% 44%;
    background: var(--peach-art);
  }
  .label--sage .label__art { background: var(--sage-art); }
  .label__detail {
    position: absolute;
    font-size: 12px;
  }

  /* Tall tin label */
  .label--tall-top { left: 564px; top: 170px; width: 186px; height: 303px; }
  .label--tall-bottom { left: 564px; top: 704px; width: 186px; height: 302px; }
  .label--earl-grey { left: 868px; top: 704px; width: 186px; height: 302px; }
  .label--square { left: 116px; top: 790px; width: 270px; height: 268px; }

  /* Round lid label */
  .round-label {
    position: absolute;
    left: 60px;
    top: 216px;
    width: 312px;
    height: 312px;
    border-radius: 50%;
    background: var(--peach);
  }
  .round-label__title {
    position: absolute;
    left: 105px;
    top: 44px;
    font-size: 23px;
    line-height: 1.05;
  }
  .round-label__side {
    position: absolute;
    font-size: 11.5px;
    white-space: nowrap;
  }
  .round-label__side--left {
    left: -4px;
    top: 150px;
    transform: rotate(-72deg);
  }
  .round-label__side--right {
    left: 188px;
    top: 146px;
    transform: rotate(78deg);
  }
  .round-label__art {
    position: absolute;
    left: 96px;
    top: 104px;
    width: 132px;
    height: 118px;
    border-radius: 50% 50% 44% 44%;
    background: var(--peach-art);
  }
  .round-label__tagline {
    position: absolute;
    left: 140px;
    top: 240px;
    font-size: 12px;
    line-height: 1.3;
  }

  /* Lid seal */
  .hood-caption {
    position: absolute;
    left: 900px;
    top: 270px;
    width: 120px;
    text-align: center;
    font-size: 11px;
    font-weight: 700;
    color: var(--label-white);
  }
  .seal {
    position: absolute;
    left: 894px;
    top: 354px;
    width: 132px;
    height: 132px;
    border-radius: 50%;
    background: var(--sage);
    display: flex;
    flex-direction: column;
    align-items: center;
    justify-content: center;
    text-align: center;
    gap: 6px;
  }
  .seal__name {
    font-size: 12px;
    line-height: 1.2;
    width: 96px;
  }
  .seal__motto {
    font-size: 9px;
    width: 100px;
  }
</style>
</head>
<body>

  <!-- Lid top: round label -->
  <section class="round-label">
    <h2 class="round-label__title">ENGLISH<br>BREAKFAST</h2>
    <p class="round-label__side round-label__side--left">Tarrowby Tea Company</p>
    <p class="round-label__side round-label__side--right">100% pure tea 8 Oz.; 250g</p>
    <div class="round-label__art" role="img" aria-label="Line drawing of a teapot with a tea leaf inside"></div>
    <p class="round-label__tagline">It's your moment.<br>Enjoy it !</p>
  </section>

  <!-- Tall tin -->
  <section class="label label--tall-top">
    <p class="label__brand" style="left:18px; top:16px;">TarrowbyTeaCo.</p>
    <h2 class="label__title" style="left:18px; top:36px;">ENGLISH<br>BREAKFAST</h2>
    <p class="label__tagline" style="left:18px; top:92px;">It's your moment. Enjoy it !</p>
    <div class="label__art" style="left:28px; top:120px; width:130px; height:104px;" role="img" aria-label="Line drawing of a teapot with a tea leaf inside"></div>
    <p class="label__detail" style="left:18px; top:252px;">8 Oz.</p>
    <p class="label__detail" style="left:136px; top:252px;">250g</p>
    <p class="label__detail" style="left:18px; top:272px;">100% pure tea</p>
  </section>

  <!-- Lid seal -->
  <p class="hood-caption">THE HOOD</p>
  <div class="seal">
    <p class="seal__name">Tarrowby Tea Company</p>
    <p class="seal__motto">Keep it simple. Drink tea !</p>
  </div>

  <!-- Square tin -->
  <section class="label label--square">
    <p class="label__brand" style="left:176px; top:16px;">TarrowbyTeaCo.</p>
    <h2 class="label__title" style="left:22px; top:16px;">ENGLISH<br>BREAKFAST</h2>
    <p class="label__tagline" style="left:22px; top:72px;">It's your moment. Enjoy it !</p>
    <div class="label__art" style="left:64px; top:96px; width:170px; height:140px;" role="img" aria-label="Line drawing of a steaming teapot with a tea leaf inside"></div>
    <p class="label__detail" style="left:22px; top:216px;">8 Oz.</p>
    <p class="label__detail" style="left:22px; top:238px;">100% pure tea</p>
    <p class="label__detail" style="left:218px; top:238px;">250g</p>
  </section>

  <!-- Round tin, English Breakfast -->
  <section class="label label--tall-bottom">
    <p class="label__brand" style="left:18px; top:16px;">TarrowbyTeaCo.</p>
    <h2 class="label__title" style="left:18px; top:36px;">ENGLISH<br>BREAKFAST</h2>
    <p class="label__tagline" style="left:18px; top:92px;">It's your moment. Enjoy it !</p>
    <div class="label__art" style="left:28px; top:120px; width:130px; height:104px;" role="img" aria-label="Line drawing of a teapot with a shaded tea leaf inside"></div>
    <p class="label__detail" style="left:18px; top:252px;">8 Oz.</p>
    <p class="label__detail" style="left:136px; top:252px;">250g</p>
    <p class="label__detail" style="left:18px; top:272px;">100% pure tea</p>
  </section>

  <!-- Round tin, Earl Grey -->
  <section class="label label--earl-grey label--sage">
    <p class="label__brand" style="left:18px; top:16px;">TarrowbyTeaCo.</p>
    <h2 class="label__title" style="left:18px; top:48px;">EARL GREY</h2>
    <p class="label__tagline" style="left:18px; top:92px;">It's your moment. Enjoy it !</p>
    <div class="label__art" style="left:22px; top:116px; width:142px; height:112px;" role="img" aria-label="Line drawing of a steaming teapot with a tea leaf inside"></div>
    <p class="label__detail" style="left:18px; top:252px;">8 Oz.</p>
    <p class="label__detail" style="left:136px; top:252px;">250g</p>
    <p class="label__detail" style="left:18px; top:272px;">100% pure tea</p>
  </section>

</body>
</html>
```